Harborline Toma's Chinese/Dim Sum Restaurant Menu

Harborline Toma's is a seafood-asian fusion restaurant featuring dim sum and other classical asian fusion items.

We need a menu design that includes both our food menu and our drink menu.

Food menu: Needs to have space for descriptions of food (please just include a place holder and we will input them later). See attached for food menu items.

Drink menu: Just lists of items with prices. See attached Jade Lantern Menu- please include the same items, but rebrand for Harborline Toma's.

The menus must be able to be printed in a 4.25x11in paper.

We want something modern and contemporary. My boss likes geometrical design aspects and minimalism. So, nothing too ornate. But, it has to be different from the Jade Lantern menus. Colors can be black, red, gold or blue- but it must be able to be tied into our black and red Harborline Toma's logo. Including elements of Chinese culture, especially fishing, is a plus, but not necessary.

We also need this in ai format when we download final copy so we can edit in the future.

UPDATE: Please note, we already have a logo.

Target Market(s)

Upscale family diners

Industry/Entity Type

Chinese Food

Font styles to use
Serif
Sans Serif

Colors
0054AA
0677BA
7BADD7
CADEEF
E8F1F8
0094D4
00A9DD
6FCCEA
C7EBF8
E9F6FB
FFC000
F8CF3A
FAE287
FDF2CF
FEFAEE
EB3D1F
EC4F4E
F09395
F8D3D4
FCEDEE

Requirements
Must have
• Classic, minimalist, elegant

```html
<!DOCTYPE html>
<html lang="en">
<head>
<meta charset="utf-8">
<title>Harborline Toma's — Dim Sum Menu</title>
<link rel="stylesheet" href="https://fonts.googleapis.com/css2?family=Bodoni+Moda:ital,wght@0,400;1,400&family=Open+Sans:wght@400&display=swap">
<style>
  :root {
    --red: #c8151b;
    --red-soft: #e23a3a;
    --ink: #111111;
    --paper: #ffffff;
  }
  * { margin: 0; padding: 0; box-sizing: border-box; }
  html, body {
    width: 1200px;
    height: 3196px;
    overflow: hidden;
    background: var(--paper);
  }
  .menu {
    position: relative;
    width: 1200px;
    height: 3196px;
    background: var(--paper);
    color: var(--ink);
  }
  .brand {
    position: absolute;
    top: 240px;
    left: 0;
    width: 1200px;
    text-align: center;
    font-family: "Bodoni Moda", serif;
    font-weight: 400;
    font-size: 84px;
    line-height: 100px;
    color: var(--ink);
  }
  .section-banner {
    position: absolute;
    top: 560px;
    left: 368px;
    width: 440px;
    height: 84px;
    background: var(--red);
    color: var(--paper);
    font-family: "Bodoni Moda", serif;
    font-weight: 400;
    font-size: 56px;
    line-height: 84px;
    text-align: center;
    letter-spacing: 2px;
  }
  .dish {
    position: absolute;
    left: 0;
    width: 1200px;
    height: 330px;
  }
  .dish__photo {
    position: absolute;
    left: 0;
    top: 0;
    width: 330px;
    height: 330px;
  }
  .dish__photo-label {
    position: absolute;
    left: 0;
    top: 0;
    width: 330px;
    height: 330px;
    line-height: 330px;
    text-align: center;
    font-family: "Open Sans", sans-serif;
    font-size: 44px;
    color: var(--ink);
  }
  .dish__rule {
    position: absolute;
    left: 310px;
    top: 150px;
    width: 850px;
    height: 3px;
    background: var(--red-soft);
  }
  .dish__name {
    position: absolute;
    left: 328px;
    top: 69px;
    font-family: "Bodoni Moda", serif;
    font-weight: 400;
    font-size: 52px;
    line-height: 60px;
    color: var(--ink);
    white-space: nowrap;
  }
  .dish__price {
    position: absolute;
    right: 40px;
    top: 88px;
    font-family: "Bodoni Moda", serif;
    font-style: italic;
    font-weight: 400;
    font-size: 32px;
    line-height: 38px;
    color: var(--ink);
  }
  .dish__desc {
    position: absolute;
    left: 330px;
    top: 194px;
    font-family: "Bodoni Moda", serif;
    font-style: italic;
    font-weight: 400;
    font-size: 32px;
    line-height: 40px;
    color: var(--ink);
  }
</style>
</head>
<body>
<main class="menu">
  <header class="brand">Harborline Toma's</header>

  <h1 class="section-banner">DIM SUM</h1>

  <article class="dish" style="top:728px">
    <svg class="dish__photo" viewBox="0 0 330 330" role="img" aria-label="Photo of potstickers">
      <circle cx="165" cy="165" r="160" fill="var(--paper)" stroke="var(--red)" stroke-width="5"/>
    </svg>
    <span class="dish__photo-label">Photo here</span>
    <div class="dish__rule"></div>
    <h2 class="dish__name">Potsticker</h2>
    <span class="dish__price">$12</span>
    <p class="dish__desc">Menu description here</p>
  </article>

  <article class="dish" style="top:1086px">
    <svg class="dish__photo" viewBox="0 0 330 330" role="img" aria-label="Photo of plant-based dumplings">
      <circle cx="165" cy="165" r="160" fill="var(--paper)" stroke="var(--red)" stroke-width="5"/>
    </svg>
    <span class="dish__photo-label">Photo here</span>
    <div class="dish__rule"></div>
    <h2 class="dish__name">Verdant Dumpling</h2>
    <span class="dish__price">$11</span>
    <p class="dish__desc">Menu description here</p>
  </article>

  <article class="dish" style="top:1444px">
    <svg class="dish__photo" viewBox="0 0 330 330" role="img" aria-label="Photo of lobster dumplings">
      <circle cx="165" cy="165" r="160" fill="var(--paper)" stroke="var(--red)" stroke-width="5"/>
    </svg>
    <span class="dish__photo-label">Photo here</span>
    <div class="dish__rule"></div>
    <h2 class="dish__name">Lobster Dumpling</h2>
    <span class="dish__price">$13</span>
    <p class="dish__desc">Menu description here</p>
  </article>

  <article class="dish" style="top:1802px">
    <svg class="dish__photo" viewBox="0 0 330 330" role="img" aria-label="Photo of sticky rice">
      <circle cx="165" cy="165" r="160" fill="var(--paper)" stroke="var(--red)" stroke-width="5"/>
    </svg>
    <span class="dish__photo-label">Photo here</span>
    <div class="dish__rule"></div>
    <h2 class="dish__name">Sticky Rice</h2>
    <span class="dish__price">$5</span>
    <p class="dish__desc">Menu description here</p>
  </article>

  <article class="dish" style="top:2160px">
    <svg class="dish__photo" viewBox="0 0 330 330" role="img" aria-label="Photo of pork siu mai">
      <circle cx="165" cy="165" r="160" fill="var(--paper)" stroke="var(--red)" stroke-width="5"/>
    </svg>
    <span class="dish__photo-label">Photo here</span>
    <div class="dish__rule"></div>
    <h2 class="dish__name">Pork Siu Mai</h2>
    <span class="dish__price">$12</span>
    <p class="dish__desc">Menu description here</p>
  </article>

  <article class="dish" style="top:2518px">
    <svg class="dish__photo" viewBox="0 0 330 330" role="img" aria-label="Photo of spicy won ton">
      <circle cx="165" cy="165" r="160" fill="var(--paper)" stroke="var(--red)" stroke-width="5"/>
    </svg>
    <span class="dish__photo-label">Photo here</span>
    <div class="dish__rule"></div>
    <h2 class="dish__name">Spicy Won Ton</h2>
    <span class="dish__price">$12</span>
    <p class="dish__desc">Menu description here</p>
  </article>

  <article class="dish" style="top:2866px">
    <svg class="dish__photo" viewBox="0 0 330 330" role="img" aria-label="Photo of vegan spicy won ton">
      <circle cx="165" cy="165" r="160" fill="var(--paper)" stroke="var(--red)" stroke-width="5"/>
    </svg>
    <span class="dish__photo-label">Photo here</span>
    <div class="dish__rule"></div>
    <h2 class="dish__name">Vegan Spicy Won Ton</h2>
    <span class="dish__price">$12</span>
    <p class="dish__desc">Menu description here</p>
  </article>
</main>
</body>
</html>
```